Business Card/Stationary
General Contractor
Thank You for all of the submissions so far.
I have eliminated those that had too many curved lines. I like any lines to be more perpendicular/parallel. However, I have left a few with curved lines that I like.
I do like the solid colors on the front and or back.
I have not seen any stationary submissions. I need some of those as well, although not as critical as a business card.
Thank You for your submissions. I will comment again in a couple of days.

```html
<!DOCTYPE html>
<html lang="en">
<head>
<meta charset="utf-8">
<title>KorvMint Builders – Stationery Set</title>
<link rel="stylesheet" href="https://fonts.googleapis.com/css2?family=Questrial&display=swap">
<style>
  :root {
    --board: #8b8b8b;
    --paper: #ffffff;
    --ink: #4a4a4a;
    --ink-soft: #8a8a8a;
    --brand-blue: #1f4ea3;
    --brand-blue-dark: #173b7e;
    --brand-orange: #f28c1c;
    --brand-orange-deep: #e0701a;
    --rule: #d6d6d6;
  }
  * { box-sizing: border-box; margin: 0; padding: 0; }
  html, body { width: 1200px; height: 662px; overflow: hidden; }
  body {
    background: var(--board);
    font-family: "Questrial", sans-serif;
    color: var(--ink);
    position: relative;
  }
  .sheet { position: absolute; background: var(--paper); box-shadow: 0 1px 3px rgba(0,0,0,.25); }
  .edge-band { position: absolute; top: 0; right: 0; bottom: 0; width: 6px; background: var(--brand-blue); }

  .wordmark { position: absolute; display: flex; align-items: center; gap: 8px; }
  .wordmark-square { background: var(--brand-orange); flex: none; }
  .wordmark-text { color: var(--ink); line-height: 1; }
  .wordmark-text small { display: block; font-size: .3em; letter-spacing: .12em; margin-top: 3px; color: var(--ink-soft); }

  .fine { font-size: 7px; line-height: 1.45; color: var(--ink-soft); position: absolute; white-space: nowrap; }

  /* Letterhead */
  .letterhead { left: 187px; top: 19px; width: 442px; height: 617px; }
  .letterhead .wordmark { left: 20px; top: 24px; }
  .letterhead .wordmark-square { width: 30px; height: 30px; }
  .letterhead .wordmark-text { font-size: 34px; }
  .letterhead .fine-left { left: 22px; bottom: 18px; }
  .letterhead .fine-right { right: 22px; bottom: 18px; }

  /* Business cards */
  .card { width: 149px; height: 117px; left: 36px; }
  .card-back {
    top: 233px;
    background: linear-gradient(135deg, var(--brand-orange) 0%, var(--brand-orange-deep) 100%);
    overflow: hidden;
  }
  .card-back .emblem-area {
    position: absolute; left: 46px; top: 16px; width: 58px; height: 58px;
    background: rgba(255,255,255,.12);
  }
  .card-back .tagline { position: absolute; left: 0; right: 0; top: 80px; text-align: center; font-size: 5px; line-height: 1.5; color: #fff3e0; white-space: nowrap; }

  .card-front { top: 351px; display: flex; overflow: hidden; }
  .card-front .card-logo-side { width: 65px; position: relative; }
  .card-front .wordmark { left: 6px; top: 48px; gap: 4px; }
  .card-front .wordmark-square { width: 9px; height: 9px; }
  .card-front .wordmark-text { font-size: 11px; }
  .card-front .card-info-side {
    flex: 1; background: linear-gradient(160deg, var(--brand-blue) 0%, var(--brand-blue-dark) 100%);
    position: relative; color: #e6ecf7; white-space: nowrap;
  }
  .card-info-side .holder { position: absolute; left: 30px; top: 12px; font-size: 5.5px; line-height: 1.4; }
  .card-info-side .holder strong { font-weight: 400; font-size: 6px; display: block; }
  .card-info-side .contact { position: absolute; left: 44px; top: 52px; font-size: 4.5px; line-height: 1.5; }
  .card-info-side .address { position: absolute; left: 30px; bottom: 10px; font-size: 4.5px; line-height: 1.5; }

  /* Envelopes */
  .envelope { left: 665px; width: 497px; }
  .envelope-back { top: 96px; height: 223px; }
  .envelope-back svg { position: absolute; inset: 0; }
  .envelope-back .wordmark { left: 232px; top: 26px; }
  .envelope-back .wordmark-square { width: 26px; height: 26px; }

  .envelope-front { top: 343px; height: 286px; }
  .envelope-front .wordmark { left: 24px; top: 34px; }
  .envelope-front .wordmark-square { width: 30px; height: 30px; }
  .envelope-front .wordmark-text { font-size: 34px; }
  .envelope-front .fine-left { left: 26px; bottom: 34px; }
  .envelope-front .fine-right { right: 72px; bottom: 34px; }
</style>
</head>
<body>

  <section class="sheet letterhead" aria-label="Letterhead">
    <div class="wordmark">
      <span class="wordmark-square"></span>
      <span class="wordmark-text">KorvMint<small>BUILDERS, LLC</small></span>
    </div>
    <div class="fine fine-left">
      info@korvmint.com<br>
      1420 Harlow Street, Suite 3<br>
      Fort Lane, TX 75010
    </div>
    <div class="fine fine-right">
      Tel 555 010 2040<br>
      Fax 555 010 2041<br>
      Cel 555 010 2042
    </div>
    <span class="edge-band"></span>
  </section>

  <section class="sheet card card-back" aria-label="Business card back">
    <div class="emblem-area" role="img" aria-label="Large faint brand emblem area"></div>
    <p class="tagline">General Contractor<br>Residential &amp; Commercial Building</p>
  </section>

  <section class="sheet card card-front" aria-label="Business card front">
    <div class="card-logo-side">
      <div class="wordmark">
        <span class="wordmark-square"></span>
        <span class="wordmark-text">KorvMint</span>
      </div>
    </div>
    <div class="card-info-side">
      <p class="holder"><strong>Dana R. Holt</strong>President</p>
      <p class="contact">T 555 010 2040<br>F 555 010 2041<br>C 555 010 2042</p>
      <p class="address">info@korvmint.com<br>1420 Harlow Street<br>Fort Lane, TX</p>
    </div>
  </section>

  <section class="sheet envelope envelope-back" aria-label="Envelope back">
    <svg width="497" height="223" viewBox="0 0 497 223" aria-hidden="true">
      <path d="M0 4 Q 120 8 200 78 Q 248 112 296 78 Q 376 8 491 4" fill="none" stroke="var(--rule)" stroke-width="1"/>
    </svg>
    <div class="wordmark">
      <span class="wordmark-square"></span>
    </div>
    <span class="edge-band"></span>
  </section>

  <section class="sheet envelope envelope-front" aria-label="Envelope front">
    <div class="wordmark">
      <span class="wordmark-square"></span>
      <span class="wordmark-text">KorvMint<small>BUILDERS, LLC</small></span>
    </div>
    <div class="fine fine-left">
      info@korvmint.com<br>
      1420 Harlow Street, Suite 3<br>
      Fort Lane, TX 75010
    </div>
    <div class="fine fine-right">
      Tel 555 010 2040<br>
      Fax 555 010 2041<br>
      Cel 555 010 2042
    </div>
    <span class="edge-band"></span>
  </section>

</body>
</html>
```